PACKAGING DESIGN NEEDED - TEMPLATE SUPPLIED - UPDATED BRAND MEADOW

Our company needs submissions for an outer box similar to a cereal box which will house sachets of instant Yoghurt Mix

I have attached a template for the core design and the correct varietals and nutrition info can be inserted later

We need 2 boxes

1- Natural Greek Yoghurt x 4 Sachets

2- Natural Greek Yoghurt with Honey x 2 Sachets and Boysenberry Yoghurt x 2 Sachets

I am initially looking for a design concept and the finer details can be inserted later

Our contract manufacturer has a website that may assist with preliminary ideas and you can see the sachets but not the boxes. We will not be printing sachets so we focus on the box but the website will assist.

http://www.corvellidairy.example/au/

I have also attached some shots of the companies other brand which features and animated cow so it can again synch you with their style.

The Brand is now MEADOW and another logo can be created with this name for the excercise....Animated cow could be used or similar

Thanks
Tomas

Target Market(s)

China

Industry/Entity Type

It Company

Font styles to use
Sans Serif

Requirements
Must have
• Clean and Fresh looking

```html
<!DOCTYPE html>
<html lang="en">
<head>
<meta charset="utf-8">
<title>Meadow Yoghurt Mix – Box Dieline</title>
<link rel="stylesheet" href="https://fonts.googleapis.com/css2?family=Quicksand:wght@700&family=Roboto+Condensed:wght@400&display=swap">
<style>
  :root {
    --paper: #ffffff;
    --cut: #e8231f;
    --crease: #33dd33;
    --dim: #9a9a3a;
    --dim-line: #c9c99a;
    --band-dark: #2c3f8f;
    --band-mid: #5a72c4;
    --band-light: #8fa3df;
    --panel-white: #f7f9fc;
    --brand: #3b4fa3;
    --bar-1: #aab6df;
    --bar-2: #8f9fd6;
    --bar-3: #7488cc;
  }
  html, body {
    margin: 0;
    padding: 0;
    width: 1200px;
    height: 885px;
    overflow: hidden;
    background: var(--paper);
  }
  .dieline { display: block; width: 1200px; height: 885px; }
  .cut { fill: none; stroke: var(--cut); stroke-width: 1.3; stroke-linejoin: miter; }
  .crease { fill: none; stroke: var(--crease); stroke-width: 1.3; }
  .dim-line { stroke: var(--dim-line); stroke-width: 0.8; fill: none; }
  .dim-label { fill: var(--dim); font-family: "Roboto Condensed", sans-serif; font-size: 13px; }
  .spec-note { fill: var(--cut); font-family: "Roboto Condensed", sans-serif; font-size: 11.5px; }
  .panel-white { fill: var(--panel-white); }
  .brand-name { fill: var(--brand); font-family: "Quicksand", sans-serif; font-weight: 700; }
  .bar-1 { fill: var(--bar-1); }
  .bar-2 { fill: var(--bar-2); }
  .bar-3 { fill: var(--bar-3); }
</style>
</head>
<body>
<svg class="dieline" viewBox="0 0 1100 811" preserveAspectRatio="none" xmlns="http://www.w3.org/2000/svg">
  <defs>
    <linearGradient id="band-tone" x1="0" y1="0" x2="1" y2="1">
      <stop offset="0" stop-color="var(--band-mid)"/>
      <stop offset="0.5" stop-color="var(--band-dark)"/>
      <stop offset="1" stop-color="var(--band-light)"/>
    </linearGradient>
  </defs>

  <g class="dimensions">
    <line class="dim-line" x1="32" y1="18" x2="32" y2="721"/>
    <line class="dim-line" x1="50" y1="18" x2="50" y2="721"/>
    <line class="dim-line" x1="32" y1="18" x2="860" y2="18"/>
    <line class="dim-line" x1="50" y1="197" x2="97" y2="197"/>
    <line class="dim-line" x1="50" y1="313" x2="70" y2="313"/>
    <line class="dim-line" x1="50" y1="567" x2="97" y2="567"/>
    <line class="dim-line" x1="32" y1="721" x2="107" y2="721"/>
    <line class="dim-line" x1="70" y1="721" x2="70" y2="752"/>
    <line class="dim-line" x1="70" y1="738" x2="1083" y2="738"/>
    <line class="dim-line" x1="97" y1="750" x2="1083" y2="750"/>
    <line class="dim-line" x1="97" y1="721" x2="97" y2="752"/>
    <line class="dim-line" x1="357" y1="721" x2="357" y2="742"/>
    <line class="dim-line" x1="591" y1="721" x2="591" y2="742"/>
    <line class="dim-line" x1="849" y1="721" x2="849" y2="742"/>
    <line class="dim-line" x1="1083" y1="580" x2="1083" y2="752"/>

    <text class="dim-label" transform="translate(55 108) rotate(-90)" text-anchor="middle">101.75</text>
    <text class="dim-label" transform="translate(55 256) rotate(-90)" text-anchor="middle">65.5</text>
    <text class="dim-label" transform="translate(37 370) rotate(-90)" text-anchor="middle">398.75</text>
    <text class="dim-label" transform="translate(55 440) rotate(-90)" text-anchor="middle">143.5</text>
    <text class="dim-label" transform="translate(55 645) rotate(-90)" text-anchor="middle">88</text>

    <text class="dim-label" x="84" y="743" text-anchor="middle">15</text>
    <text class="dim-label" x="227" y="743" text-anchor="middle">147</text>
    <text class="dim-label" x="474" y="743" text-anchor="middle">132</text>
    <text class="dim-label" x="575" y="755" text-anchor="middle">573</text>
    <text class="dim-label" x="720" y="743" text-anchor="middle">147</text>
    <text class="dim-label" x="966" y="743" text-anchor="middle">132</text>
  </g>

  <g class="print-area">
    <rect class="panel-white" x="97" y="313" width="986" height="254"/>
    <rect x="97" y="313" width="986" height="44" fill="url(#band-tone)" role="img" aria-label="Blue low-poly faceted pattern band"/>
    <rect x="97" y="521" width="986" height="46" fill="url(#band-tone)" role="img" aria-label="Blue low-poly faceted pattern band"/>

    <rect class="bar-1" x="97" y="362" width="123" height="19" rx="9.5"/>
    <rect class="bar-2" x="97" y="387" width="146" height="19" rx="9.5"/>
    <rect class="bar-3" x="97" y="412" width="169" height="19" rx="9.5"/>

    <text class="brand-name" x="124" y="501" font-size="50">Meadow</text>
    <text class="brand-name" x="372" y="501" font-size="51">Meadow</text>
    <text class="brand-name" x="638" y="505" font-size="37">Meadow</text>
  </g>

  <g class="creases">
    <line class="crease" x1="97" y1="313" x2="1083" y2="313"/>
    <line class="crease" x1="97" y1="567" x2="1083" y2="567"/>
    <line class="crease" x1="357" y1="313" x2="357" y2="567"/>
    <line class="crease" x1="591" y1="313" x2="591" y2="567"/>
    <line class="crease" x1="849" y1="313" x2="849" y2="567"/>
    <line class="crease" x1="97" y1="313" x2="97" y2="567"/>
    <line class="crease" x1="868" y1="55" x2="1063" y2="55"/>
    <line class="crease" x1="240" y1="684" x2="353" y2="572"/>
    <line class="crease" x1="733" y1="684" x2="846" y2="572"/>
  </g>

  <g class="cuts">
    <path class="cut" d="M97 313 L70 323 L70 545 L97 567"/>
    <path class="cut" d="M97 313 L97 197 L322 197 L348 290 L352 297 L353 310 L357 313"/>
    <path class="cut" d="M357 313 L591 313"/>
    <path class="cut" d="M591 313 L594 300 L598 295 L622 197 L849 197"/>
    <path class="cut" d="M849 313 L849 53 L853 53 Q850 18 875 18 L1058 18 Q1083 18 1080 53 L1083 53 L1083 567"/>
    <path class="cut" d="M97 567 L107 721 L195 721 L227 690 L227 684 L240 684 L278 721 L353 721 L353 578 L357 567"/>
    <path class="cut" d="M357 567 L402 684 L474 684 L591 567"/>
    <path class="cut" d="M591 567 L598 721 L688 721 L720 690 L720 684 L733 684 L770 721 L846 721 L846 578 L849 567"/>
    <path class="cut" d="M849 567 L895 684 L965 684 L1083 580 L1083 567"/>
  </g>

  <g class="job-spec">
    <text class="spec-note" x="6" y="742">PRINT FACE</text>
    <text class="spec-note" x="6" y="756">P007318</text>
    <text class="spec-note" x="6" y="770">SIZE:132X147X143.5</text>
    <text class="spec-note" x="6" y="784">OA:398.75X573</text>
    <text class="spec-note" x="6" y="798">LUMEN 650MIC</text>
  </g>
</svg>
</body>
</html>
```